Kelvara Pay & Fintech Solutions needs a business card design and logo

I need the design of a business card and a logo for my consultant, based in Asuncion Paraguay. I am in the Digital World category, specializing in Kelvara Pay, Fintech Solutions & e-commerce. I would like the design to reflect trust and above all encompass the area of ​​specialty of the services that I offer. (Kelvara Pay, Fintech Solutions & e-commerce)

Target Market(s)

Financial entities, companies wishing to undertake a Fintech or e-commerce project

Contact Information for Business Card

Marisol Quenderra
Senior Advisory Consultant
Cel +595982417305
Skype ID marisolquenderra
Linkedin: http://lnkvo.example/7wqpzjT

Logo Text

Fintech Solutions&E-commerce

Requirements
Must have
• I would like it to be a fusion of symbols, example of the @, the $, cellular (cell) that can encompass the areas.
Nice to have
• Must be related to the Fintech area and / or Kelvara Pay and e-commerce. It is a new consultancy, so there are no previous logos

```html
<!DOCTYPE html>
<html lang="en">
<head>
<meta charset="utf-8">
<title>Kelvara Pay – Business Card</title>
<link href="https://fonts.googleapis.com/css2?family=Bree+Serif&family=Open+Sans:wght@400;600&display=swap" rel="stylesheet">
<style>
  :root {
    --backdrop: #cacaca;
    --navy: #2c5480;
    --navy-soft: #3a6694;
    --paper: #f9f9f9;
    --orange: #e87b1c;
    --grey-text: #8a8a8a;
    --ink: #1e1e1e;
    --white: #ffffff;
  }
  * { margin: 0; padding: 0; box-sizing: border-box; }
  html, body { width: 1200px; height: 1005px; overflow: hidden; }
  body {
    background: var(--backdrop);
    position: relative;
    font-family: "Open Sans", sans-serif;
  }
  .card {
    position: absolute;
    left: 250px;
    width: 700px;
    height: 400px;
    overflow: hidden;
  }
  .card--back { top: 70px; background: var(--navy); }
  .card--front { top: 535px; background: var(--paper); }

  /* back side */
  .back-mark {
    position: absolute;
    left: 50%;
    top: 70px;
    transform: translateX(-50%);
    width: 120px;
    height: 120px;
    border-radius: 50%;
    border: 10px solid var(--white);
  }
  .back-brand {
    position: absolute;
    left: 0; right: 0;
    top: 230px;
    text-align: center;
    color: var(--white);
  }
  .brand-name {
    font-family: "Bree Serif", serif;
    font-size: 52px;
    line-height: 1;
  }
  .brand-tagline {
    font-family: "Bree Serif", serif;
    font-size: 20px;
    margin-top: 6px;
  }

  /* front side */
  .front-band {
    position: absolute;
    left: 0; right: 0; bottom: 0;
    height: 100px;
    background: linear-gradient(90deg, var(--navy-soft), var(--navy));
  }
  .front-brand {
    position: absolute;
    left: 50px;
    top: 44px;
    display: flex;
    align-items: center;
    gap: 18px;
  }
  .front-mark {
    width: 78px; height: 78px;
    border-radius: 50%;
    border: 9px solid var(--orange);
    flex: none;
  }
  .front-brand .brand-name { color: var(--navy); font-size: 56px; }
  .front-brand .brand-tagline { color: var(--grey-text); font-size: 24px; margin-top: 2px; }

  .person {
    position: absolute;
    left: 60px;
    top: 165px;
    color: var(--ink);
  }
  .person-name {
    font-family: "Bree Serif", serif;
    color: var(--navy);
    font-size: 32px;
    line-height: 1;
  }
  .person-role { font-size: 15px; margin-top: 4px; }
  .person-address { font-size: 15px; line-height: 1.6; margin-top: 14px; }

  .contact {
    position: absolute;
    right: 26px;
    bottom: 14px;
    list-style: none;
    color: var(--white);
    font-size: 16px;
    text-align: right;
    line-height: 1.5;
  }
  .contact li { display: flex; justify-content: flex-end; align-items: center; gap: 10px; }
  .contact svg { width: 14px; height: 14px; fill: var(--white); flex: none; }
</style>
</head>
<body>

<section class="card card--back">
  <div class="back-mark"></div>
  <div class="back-brand">
    <div class="brand-name">Kelvara Pay</div>
    <div class="brand-tagline">fintech solutions &amp; e-commerce</div>
  </div>
</section>

<section class="card card--front">
  <div class="front-band" role="img" aria-label="Decorative navy wave with green and orange accent lines"></div>

  <div class="front-brand">
    <div class="front-mark"></div>
    <div>
      <div class="brand-name">Kelvara Pay</div>
      <div class="brand-tagline">fintech solutions &amp; e-commerce</div>
    </div>
  </div>

  <div class="person">
    <div class="person-name">Your Name</div>
    <div class="person-role">Director</div>
    <div class="person-address">123, Street No., City Name,<br>Country 123456</div>
  </div>

  <ul class="contact">
    <li>000-111-2222
      <svg viewBox="0 0 16 16"><path d="M1 6c0-2 3-3 7-3s7 1 7 3v1h-4V6H5v1H1zM4 8h8l2 6H2z"/></svg></li>
    <li>www.website.com
      <svg viewBox="0 0 16 16"><path d="M1 3h14v10H1zM2 4l6 5 6-5" stroke="var(--navy)" stroke-width="1"/></svg></li>
    <li>admin@website.com
      <svg viewBox="0 0 16 16"><circle cx="8" cy="8" r="7"/><path d="M1 8h14M8 1c-3 4-3 10 0 14M8 1c3 4 3 10 0 14" stroke="var(--navy)" fill="none"/></svg></li>
  </ul>
</section>

</body>
</html>
```